High End Business Card Design for Flooring Store

Looking for a new card design for our hardwood flooring company. We have no print budget for these and are open to cards made from wood, metal, cardstock with embossed print ... or any combination of these. No plastic.

We sell luxury products and I want the cards to reflect our image of quality and class.

Our contact information as such;
Employee Name
248 Halloway Blvd.
Brayhollow, WK
E3C-4K9
(506) 555-0142
Employee email @kestraflooring.com

Target Market(s)

Home Builders

Contact Information for Business Card

Emnployee name, business contact information

```html
<!DOCTYPE html>
<html lang="en">
<head>
<meta charset="utf-8">
<title>Orvane Flooring – Business Card</title>
<link rel="stylesheet" href="https://fonts.googleapis.com/css2?family=Montserrat:wght@400;500;700&display=swap">
<style>
  :root {
    --page: #1a1b1e;
    --card: #26282b;
    --card-shade: #222427;
    --emboss: #121314;
    --emboss-text: #3a3c40;
    --brand-red: #a8302a;
    --brand-gold: #e8b52c;
    --muted: #7d8086;
  }
  * { box-sizing: border-box; margin: 0; padding: 0; }
  html, body {
    width: 1200px; height: 801px; overflow: hidden;
    background: var(--page);
    font-family: "Montserrat", sans-serif;
  }
  .stage {
    position: relative; width: 1200px; height: 801px;
    display: flex; align-items: center; justify-content: center; gap: 40px;
  }
  .card {
    position: relative; width: 540px; height: 309px;
    background: var(--card); overflow: hidden;
    box-shadow: 0 12px 30px rgba(0,0,0,.45);
  }

  /* Front */
  .front .brand {
    position: absolute; left: 140px; top: 108px;
    display: flex; align-items: center; gap: 12px;
  }
  .front .brand-mark { width: 26px; height: 26px; background: var(--emboss); }
  .front .brand-name {
    font-size: 58px; font-weight: 500; color: var(--emboss); line-height: 1;
  }
  .front .tagline {
    position: absolute; left: 178px; top: 180px;
    font-size: 13px; color: var(--emboss-text); line-height: 1.3;
  }

  /* Back */
  .step { position: absolute; background: var(--card-shade); }
  .step-1 { right: 0; top: 14px; width: 170px; height: 54px; }
  .step-2 { right: 0; top: 78px; width: 230px; height: 54px; }
  .step-3 { right: 0; top: 142px; width: 150px; height: 54px; }

  .back .brand {
    position: absolute; left: 36px; top: 52px;
    display: flex; align-items: center; gap: 12px;
  }
  .back .brand-mark { width: 28px; height: 28px; background: var(--brand-gold); }
  .back .brand-name {
    font-size: 62px; font-weight: 500; color: var(--brand-red); line-height: 1;
  }
  .back .tagline {
    position: absolute; left: 78px; top: 124px;
    font-size: 13px; color: var(--muted); line-height: 1.3;
  }
  .employee-name {
    position: absolute; left: 36px; top: 188px;
    font-size: 19px; font-weight: 700; letter-spacing: .5px;
    color: var(--brand-red); text-transform: uppercase;
  }
  .divider {
    position: absolute; left: 36px; right: 36px; top: 218px;
    height: 1px; background: var(--brand-gold);
  }
  .contact {
    position: absolute; left: 36px; top: 232px;
    font-size: 12px; color: var(--muted); line-height: 1.7;
  }
  .contact-line { display: flex; align-items: center; gap: 8px; }
  .contact-line svg { width: 12px; height: 12px; flex: none; }
  .address {
    position: absolute; right: 36px; top: 232px; text-align: right;
    font-size: 12px; font-style: normal; color: var(--muted); line-height: 1.45;
  }
  .base-band {
    position: absolute; left: 0; right: 0; bottom: 0; height: 7px;
    background: var(--brand-red);
  }
</style>
</head>
<body>
<main class="stage">
  <section class="card front" aria-label="Card front">
    <div class="brand">
      <span class="brand-mark"></span>
      <span class="brand-name">Orvane</span>
    </div>
    <p class="tagline">Planchers &amp; Escaliers<br>Flooring &amp; Stairs</p>
  </section>

  <section class="card back" aria-label="Card back">
    <span class="step step-1"></span>
    <span class="step step-2"></span>
    <span class="step step-3"></span>

    <div class="brand">
      <span class="brand-mark"></span>
      <span class="brand-name">Orvane</span>
    </div>
    <p class="tagline">Planchers &amp; Escaliers<br>Flooring &amp; Stairs</p>

    <p class="employee-name">Employee Name</p>
    <span class="divider"></span>

    <div class="contact">
      <p class="contact-line">
        <svg viewBox="0 0 24 24" aria-hidden="true"><path fill="#e8b52c" d="M6.6 10.8a15 15 0 0 0 6.6 6.6l2.2-2.2c.3-.3.7-.4 1-.2 1.1.4 2.3.6 3.6.6.6 0 1 .4 1 1V20c0 .6-.4 1-1 1A17 17 0 0 1 3 4c0-.6.4-1 1-1h3.5c.6 0 1 .4 1 1 0 1.3.2 2.5.6 3.6.1.3 0 .7-.2 1z"/></svg>
        (506) 555-0142
      </p>
      <p class="contact-line">
        <svg viewBox="0 0 24 24" aria-hidden="true"><rect x="2" y="5" width="20" height="14" fill="#e8b52c"/><path d="M2 5l10 8 10-8" fill="none" stroke="#26282b" stroke-width="1.6"/></svg>
        Employee email @kestraflooring.com
      </p>
    </div>

    <address class="address">
      248 Halloway Blvd.<br>Brayhollow, WK<br>E3C-4K9
    </address>

    <span class="base-band"></span>
  </section>
</main>
</body>
</html>
```